Appliance Point of Purchase Campaign

I m looking to create a campaign to be used in an applinace retail store for our extended warranty program. The theme is focused on how much people use thier appliances over the life of the warranty period. As an example, familiesv open thier fridge an average of 40x per day. I habe included a link to a file crate folder which contain our marketing assets as well as a power piint which will give you an idea of hte kind of appliances we wnat to create point of sales pieces for - stickers, posters and pop ups. Hopefully it will be self explanatory. I want prices for a fridge, washer, dishware and range.

here is a link to the folder with the powerpoint overview and some of our marketing assets. Im on a plane to rome and will be able to respond to questons when i land at about 5 AM EST.

https://www.filecrate-share.net/sh/p3vqm8wt2hx7jd/QWrtPlmZkXcvBn4HsaYeUoTi?dl=0

Target Market(s)

appliance purchasers. mothers, families

Industry/Entity Type

Appliance

Colors
33a6d7
33b8a4

Requirements
Must have
• include ideas for fridge, range, dishwasher and washer. Multiple ideas for impactful point of purchase materials that will spark discussion between a sales person and the customers
• This campaign is to drive customers to
Nice to have
• images can include real life things that might be in an appliance - dishes, ice, food etc.
• Improved copywriting with clear concise messaging
• Use our brand guidelines that are in the Filecrate folder.

```html
<!DOCTYPE html>
<html lang="en">
<head>
<meta charset="utf-8">
<title>1,000 Meals – Range Sticker</title>
<link rel="stylesheet" href="https://fonts.googleapis.com/css2?family=Figtree:wght@400;500;600&display=swap">
<style>
  :root {
    --stage: #ececec;
    --brand-blue: #0a72c9;
    --sticker-white: #ffffff;
    --rim: #1b1b1b;
    --pan-dark: #151517;
    --pan-mid: #26262a;
    --food-red: #c8362a;
    --food-salmon: #e49a86;
    --food-lemon: #e8d58a;
    --text-light: #ffffff;
  }
  html, body {
    margin: 0;
    padding: 0;
    width: 1200px;
    height: 1200px;
    overflow: hidden;
    background: var(--stage);
  }
  .canvas {
    position: relative;
    width: 1200px;
    height: 1200px;
    font-family: "Figtree", "Helvetica Neue", Arial, sans-serif;
  }
  .sticker-shape {
    position: absolute;
    inset: 0;
  }
  .headline-figure {
    position: absolute;
    left: 0;
    width: 1200px;
    top: 312px;
    margin: 0;
    text-align: center;
    font-size: 122px;
    font-weight: 600;
    letter-spacing: -5px;
    line-height: 1;
    color: var(--text-light);
  }
  .stat-copy {
    position: absolute;
    left: 302px;
    top: 459px;
    margin: 0;
    font-size: 24px;
    font-weight: 500;
    line-height: 29.5px;
    color: var(--text-light);
  }
  .plan-mark {
    position: absolute;
    left: 694px;
    top: 484px;
    display: flex;
    align-items: center;
    gap: 12px;
    color: var(--text-light);
  }
  .plan-mark__dot {
    width: 18px;
    height: 18px;
    border-radius: 50%;
    background: var(--text-light);
    flex: none;
  }
  .plan-mark__name {
    font-size: 20px;
    font-weight: 400;
    line-height: 18px;
  }
</style>
</head>
<body>
<main class="canvas">
  <svg class="sticker-shape" width="1200" height="1200" viewBox="0 0 1200 1200">
    <defs>
      <clipPath id="sticker-clip">
        <circle cx="600" cy="622" r="390"/>
      </clipPath>
      <clipPath id="photo-clip">
        <circle cx="600" cy="622" r="362"/>
      </clipPath>
      <linearGradient id="pan-tones" x1="0" y1="0" x2="1" y2="0">
        <stop offset="0" stop-color="var(--pan-dark)"/>
        <stop offset="0.14" stop-color="var(--food-red)"/>
        <stop offset="0.30" stop-color="var(--food-salmon)"/>
        <stop offset="0.46" stop-color="var(--food-red)"/>
        <stop offset="0.56" stop-color="var(--pan-mid)"/>
        <stop offset="0.72" stop-color="var(--food-lemon)"/>
        <stop offset="0.84" stop-color="var(--pan-mid)"/>
        <stop offset="1" stop-color="var(--pan-dark)"/>
      </linearGradient>
      <linearGradient id="pan-shade" x1="0" y1="0" x2="0" y2="1">
        <stop offset="0" stop-color="var(--pan-dark)" stop-opacity="0"/>
        <stop offset="0.55" stop-color="var(--pan-dark)" stop-opacity="0.25"/>
        <stop offset="1" stop-color="var(--pan-dark)" stop-opacity="0.9"/>
      </linearGradient>
    </defs>
    <circle class="sticker-rim" cx="600" cy="622" r="393" fill="var(--rim)"/>
    <g clip-path="url(#sticker-clip)">
      <rect class="sticker-base" x="200" y="220" width="800" height="800" fill="var(--sticker-white)"/>
      <rect class="sticker-band" x="200" y="220" width="800" height="398" fill="var(--brand-blue)"/>
    </g>
    <g clip-path="url(#photo-clip)" role="img" aria-label="Photo of chicken, tomato and onion skewers with lemon slices in a dark frying pan">
      <rect class="meal-photo" x="243" y="643" width="715" height="360" fill="url(#pan-tones)"/>
      <rect class="meal-photo-shade" x="243" y="643" width="715" height="360" fill="url(#pan-shade)"/>
    </g>
  </svg>

  <h1 class="headline-figure">1,000</h1>
  <p class="stat-copy">The number of meals average<br>family cooks in a year.<br>Protect me with the Appliance<br>Protection Plan.</p>

  <div class="plan-mark">
    <span class="plan-mark__dot"></span>
    <span class="plan-mark__name">Kitchenwell<br>Care<br>Plan</span>
  </div>
</main>
</body>
</html>
```